StageLoop - Music Industry App needs a top quality wordpress homepage

We need a modern responsive wordpress homepage built. Our website will only feature one page with the goal to get people to sign up to our app. A word document has been uploaded outlining the page content/sections.

Once the homepage is finalised, I will also need 2 landing pages built as part of this competition. It will be very similar to the homepage with the same layout etc but just feature different images and content. The homepage is for anyone (artists and venues) to find out about us but the landing pages will be artist or venue specific.

The completed work must be delivered as an exportable file into wordpress and be designed properly so no more work is needed to begin utilising as the actual website. The images used must be setup correctly for speed and quality also.

Target Market(s)

Venues and Artists.

Coding

Coded - Design and coding required

Requirements
Must have
• UPDATE: High Res Logo files attached
• Must be a modern looking website and be responsive. Must look good across all devices from desktop, to mobile and tablet. Needs to be very high quality.
• Please see the attached logo - I am waiting for the final high quality version and will reupload when complete but this will be enough to get you started for now. The website must have a dark base colour and have red/white elements to match the logo. The red colour used MUST match the red colour used in the logo.
• Please have a go at creating it how you think is best and provide feedback from there. I am leaving it very open to the designers so I can get the best website possible and lots of different ideas etc.

```html
<!DOCTYPE html>
<html lang="en">
<head>
<meta charset="utf-8">
<title>StageLoop – Live music booking</title>
<link rel="stylesheet" href="https://fonts.googleapis.com/css2?family=Teko:wght@500;600&family=Cabin:ital,wght@0,400;0,500;0,600;1,400&display=swap">
<style>
:root{
  --red:#e0081a;
  --red-deep:#b8020f;
  --black:#000;
  --navy:#05071a;
  --footer:#0d1a3a;
  --white:#fff;
  --green:#0fcf2a;
  --card:#f4f4f4;
  --muted:#9a9ab8;
  --ink:#222;
}
*{box-sizing:border-box;margin:0;padding:0}
html,body{width:1200px;height:3759px;overflow:hidden}
body{position:relative;background:var(--black);font-family:"Cabin",sans-serif;color:var(--white)}
.abs{position:absolute}
.display{font-family:"Teko",sans-serif;font-weight:500;line-height:1}

/* hero */
.hero{left:0;top:0;width:1200px;height:600px;background:linear-gradient(180deg,#4a1ab0 0%,#3a128e 30%,#1a0840 60%,#000 100%)}
.brand{left:175px;top:28px;display:flex;align-items:center;gap:10px;font-weight:600;font-size:30px;color:var(--white)}
.brand .dot{width:26px;height:26px;border-radius:50%;background:var(--red)}
.nav{right:186px;top:16px;display:flex;gap:32px;font-size:11px;color:#c9bff0}
.nav .on{color:var(--white)}
.hero-title{left:0;width:1200px;top:150px;text-align:center;font-family:"Teko",sans-serif;font-weight:600;font-size:118px;line-height:.82}
.hero-sub{left:0;width:1200px;top:365px;text-align:center;font-size:17px}
.signup{display:flex;align-items:center}
.signup input,.signup .field{height:36px;border:0;background:var(--white);font:13px "Cabin",sans-serif;color:#999;padding:0 12px;display:flex;align-items:center}
.signup .btn{height:36px;background:var(--green);color:var(--white);font-size:11px;font-weight:600;display:flex;align-items:center;justify-content:center;text-transform:uppercase}
.hero-signup{left:326px;top:439px}
.hero-signup .lead{font-size:22px;font-weight:500;margin-right:18px}
.hero-signup .lead span{color:#5fd6e0}

/* how it works */
.how-title{left:187px;top:668px;font-size:74px}
.step-line{left:213px;top:866px;width:670px;height:1px;background:#888}
.step{width:142px}
.step .num{font-family:"Teko",sans-serif;font-size:48px;position:absolute;top:-78px;left:6px}
.step .ico{position:absolute;top:-14px;left:6px;width:28px;height:28px;border-radius:50%;background:var(--red);display:flex;align-items:center;justify-content:center}
.step .card{position:absolute;top:41px;left:0;width:142px;background:var(--card);color:#333;font-size:12.5px;line-height:1.55;padding:24px 22px}
.step .card::before{content:"";position:absolute;top:-9px;left:16px;border:9px solid transparent;border-top:0;border-bottom-color:var(--card)}

/* why */
.why-bg{left:0;top:1168px;width:1200px;height:1300px}
.why-title{left:0;width:1200px;top:1248px;text-align:center;font-size:76px}
.why-hub{left:454px;top:1361px;width:292px;height:292px;border-radius:50%;background:#000;display:flex;align-items:center;justify-content:center;gap:10px;font-size:36px;font-weight:600;box-shadow:0 6px 20px rgba(0,0,0,.5)}
.why-hub .dot{width:24px;height:24px;border-radius:50%;background:var(--red)}
.feat-ico{width:88px;height:88px;border-radius:50%;background:var(--red-deep);border:3px solid var(--white);display:flex;align-items:center;justify-content:center}
.feat h3{font-size:16px;font-weight:500;margin-bottom:6px}
.feat p{font-size:12.5px;line-height:1.55}
.feat.r{text-align:right}

/* venues / artists */
.divider{left:600px;top:1723px;width:1px;height:671px;background:rgba(255,255,255,.6)}
.col-title{width:440px;text-align:center;font-size:70px}
.bullets{list-style:none}
.bullets li{position:relative;padding-left:22px;font-size:13px;line-height:1.55;margin-bottom:11px}
.bullets li::before{content:"";position:absolute;left:0;top:6px;width:6px;height:6px;border-radius:50%;background:var(--white)}
.note{font-style:italic;font-size:12.5px;line-height:1.75}
.cta{text-align:center;font-size:24px;line-height:1}

/* about */
.about-bg{left:0;top:2467px;width:1200px;height:704px;background:radial-gradient(ellipse at 50% 100%,#8a2a1a 0%,#3a1a22 35%,#120c1e 70%,#05071a 100%)}
.about-band{left:0;top:2789px;width:1200px;height:230px;background:rgba(8,10,30,.55)}
.about-title{left:0;width:1200px;top:2578px;text-align:center;font-size:76px}
.about-sub{width:365px;text-align:center;font-size:52px}
.about-sub::after{content:"";display:block;margin:2px auto 0;width:16px;height:2px;background:var(--white)}
.about-copy p{font-size:13.5px;line-height:1.68;margin-bottom:28px}

/* contact */
.contact{left:0;top:3171px;width:1200px;height:508px;background:var(--white)}
.contact-title{left:187px;top:3282px;font-size:50px;color:var(--ink)}
.contact-title::after{content:"";display:block;width:46px;height:2px;background:var(--red);margin-top:6px}
.line-field{border-bottom:1px solid #bbb;font-size:11px;color:#888;padding-bottom:8px}
.send{left:413px;top:3537px;width:155px;height:34px;background:#000;color:var(--white);font-size:11px;font-weight:600;display:flex;align-items:center;justify-content:center}
.info{left:600px;top:3250px;width:445px;height:352px;background:#000;text-align:center}
.info .phone{font-size:29px;font-weight:500;margin-top:22px}
.info .row{font-size:11.5px;margin-top:20px}
.info .row b{font-weight:600}
.footer{left:0;top:3679px;width:1200px;height:80px;background:var(--footer);display:flex;align-items:center;justify-content:center;font-size:11px}
</style>
</head>
<body>

<!-- hero -->
<div class="abs hero" role="img" aria-label="Concert crowd with raised hands under purple stage lights"></div>
<div class="abs brand"><span class="dot"></span>StageLoop</div>
<nav class="abs nav"><span>About</span><span>How StageLoop Works</span><span>Why StageLoop?</span><span>Venues</span><span>Artists</span><span class="on">Contact</span></nav>
<h1 class="abs hero-title">ZIPR FOR<br>LIVE MUSIC</h1>
<p class="abs hero-sub">StageLoop connects venues with artists to make booking gigs simple</p>
<div class="abs signup hero-signup">
  <span class="lead">Sign up now for <span>FREE</span></span>
  <div class="field" style="width:200px">Email</div>
  <div class="btn" style="width:99px">Sign up</div>
</div>

<!-- how it works -->
<h2 class="abs display how-title">How StageLoop Works</h2>
<div class="abs step-line"></div>
<div class="abs step" style="left:197px;top:866px"><span class="num">1</span><span class="ico"><svg width="12" height="12" viewBox="0 0 12 12"><circle cx="6" cy="4" r="2.5" fill="#fff"/><path d="M1.5 11.5c0-3 2-4.5 4.5-4.5s4.5 1.5 4.5 4.5z" fill="#fff"/></svg></span><div class="card">Artists and venues sign up for free and create a profile</div></div>
<div class="abs step" style="left:363px;top:866px"><span class="num">2</span><span class="ico"><svg width="12" height="12" viewBox="0 0 12 12"><circle cx="5" cy="5" r="3" fill="none" stroke="#fff" stroke-width="2"/><path d="M7.5 7.5l3 3" stroke="#fff" stroke-width="2"/></svg></span><div class="card">Venues search for an artist for their upcoming gigs</div></div>
<div class="abs step" style="left:529px;top:866px"><span class="num">3</span><span class="ico"><svg width="13" height="12" viewBox="0 0 13 12"><ellipse cx="5" cy="5" rx="4.5" ry="3.5" fill="#fff"/><ellipse cx="8.5" cy="7" rx="4" ry="3" fill="#fff" stroke="#e0081a"/></svg></span><div class="card">Venues request a quote and communicate with the artist direct</div></div>
<div class="abs step" style="left:696px;top:866px"><span class="num">4</span><span class="ico"><svg width="10" height="12" viewBox="0 0 10 12"><rect x="1" y="1" width="8" height="10" fill="#fff"/><path d="M3 3h1M6 3h1M3 6h1M6 6h1" stroke="#e0081a"/></svg></span><div class="card">The gig is booked in once payment is provided by the venue.</div></div>
<div class="abs step" style="left:861px;top:866px"><span class="num">5</span><span class="ico"><svg width="10" height="13" viewBox="0 0 10 13"><text x="5" y="11" text-anchor="middle" fill="#fff" font-family="Cabin" font-weight="600" font-size="12">$</text></svg></span><div class="card">Upon completion the money is paid to the artist within 48 hours or less.</div></div>

<!-- why -->
<svg class="abs why-bg" viewBox="0 0 1200 1300" width="1200" height="1300" aria-hidden="true">
  <rect width="1200" height="1300" fill="#05071a"/>
  <polygon points="0,0 1190,0 0,1270" fill="#e0081a"/>
  <rect x="145" y="163" width="900" height="351" fill="#000" opacity=".08"/>
</svg>
<h2 class="abs display why-title">Why StageLoop?</h2>
<div class="abs why-hub"><span class="dot"></span>StageLoop</div>

<div class="abs feat-ico" style="left:425px;top:1362px"><svg width="46" height="38" viewBox="0 0 46 38"><ellipse cx="18" cy="15" rx="16" ry="12" fill="#fff"/><ellipse cx="29" cy="22" rx="14" ry="10" fill="#fff" stroke="#b8020f" stroke-width="2"/></svg></div>
<div class="abs feat r" style="left:209px;top:1365px;width:200px"><h3>CONNECT</h3><p>Join the StageLoop community which is full of amazing artists and venues.</p></div>

<div class="abs feat-ico" style="left:695px;top:1366px"><svg width="36" height="42" viewBox="0 0 36 42"><path d="M18 2l15 6v11c0 10-7 17-15 21C10 36 3 29 3 19V8z" fill="#fff"/><path d="M18 9l9 4v6c0 7-4 11-9 14z" fill="#b8020f"/></svg></div>
<div class="abs feat" style="left:800px;top:1363px;width:210px"><h3>PROTECTION</h3><p style="font-size:15px;line-height:1.5">Everyone is protected with our complimentary dispute resolutions.</p></div>

<div class="abs feat-ico" style="left:406px;top:1520px"><svg width="42" height="36" viewBox="0 0 42 36"><text x="2" y="12" fill="#fff" font-family="Cabin" font-weight="600" font-size="11">1</text><text x="2" y="23" fill="#fff" font-family="Cabin" font-weight="600" font-size="11">2</text><text x="2" y="34" fill="#fff" font-family="Cabin" font-weight="600" font-size="11">3</text><path d="M13 8h27M13 19h27M13 30h27" stroke="#fff" stroke-width="4"/></svg></div>
<div class="abs feat r" style="left:200px;top:1520px;width:190px"><h3>SIMPLE</h3><p>StageLoop makes gig booking easy for both the venue and artist.</p></div>

<div class="abs feat-ico" style="left:705px;top:1526px"><svg width="30" height="46" viewBox="0 0 30 46"><text x="15" y="40" text-anchor="middle" fill="#fff" font-family="Cabin" font-weight="600" font-size="44">$</text></svg></div>
<div class="abs feat" style="left:809px;top:1530px;width:190px"><h3>PRICE</h3><p>Get the best rate possible with StageLoop only receiving 5% of the artists fee</p></div>

<!-- venues / artists -->
<div class="abs divider"></div>
<h2 class="abs display col-title" style="left:157px;top:1755px">Venues</h2>
<ul class="abs bullets" style="left:204px;top:1840px;width:355px">
  <li>StageLoop is a 100% FREE service for all venues - you pay us nothing!</li>
  <li>Get instant access to hundreds of artists around your local community</li>
  <li>All genres to suit any venue from a pub to a wedding or even a nightclub</li>
  <li>Simple booking process with a money back guarantee</li>
  <li>Communicate directly with the artist and negotiate the price</li>
</ul>
<p class="abs note" style="left:194px;top:2108px;width:370px">StageLoop is not yet ready to host gigs as we're currently working on building our artists. We are launching for venues in Q4 2019. Pre-register now to keep informed and be one of the first people to use our platform.</p>
<p class="abs cta" style="left:194px;top:2229px;width:365px">Pre-register now to keep informed and be one of the first people to use our platform.</p>
<div class="abs signup" style="left:194px;top:2319px"><div class="field" style="width:219px">Email</div><div class="btn" style="width:146px">Pre register</div></div>

<h2 class="abs display col-title" style="left:602px;top:1755px">Artists</h2>
<ul class="abs bullets" style="left:650px;top:1840px;width:360px">
  <li>Sign up to StageLoop for FREE and get yourself in front of venues</li>
  <li>Only pay us if you get a gig - we only get 5% of the fee you charge the venue</li>
  <li>All genres and artists welcome - as long as you're experienced and professional</li>
  <li>Get paid within 48 hours or less after the gig guaranteed!</li>
  <li>Negotiate your price and don't pay huge agent fees to ensure you earn top dollar</li>
</ul>
<p class="abs cta" style="left:639px;top:2125px;width:367px">Sign up and create your StageLoop profile now</p>
<div class="abs signup" style="left:639px;top:2180px"><div class="field" style="width:244px">Email</div><div class="btn" style="width:123px">Sign up</div></div>

<!-- about -->
<div class="abs about-bg" role="img" aria-label="Crowd raising hands toward a performer on a red-lit stage"></div>
<div class="abs about-band"></div>
<h2 class="abs display about-title">About StageLoop</h2>
<h3 class="abs display about-sub" style="left:194px;top:2728px">About</h3>
<h3 class="abs display about-sub" style="left:639px;top:2728px">About</h3>
<div class="abs about-copy" style="left:194px;top:2806px;width:365px">
  <p>StageLoop is not yet ready to host gigs as we're currently working on building our artists. We are launching for venues in Q4 2019. Pre-register now to keep informed and be one of the first people to use our platform.</p>
  <p>StageLoop is not yet ready to host gigs as we're currently working on building our artists. We are launching for venues in Q4 2019. Pre-register now to keep informed and be one of the first people to use our platform.</p>
</div>
<div class="abs about-copy" style="left:639px;top:2806px;width:365px">
  <p>StageLoop is not yet ready to host gigs as we're currently working on building our artists. We are launching for venues in Q4 2019. Pre-register now to keep informed and be one of the first people to use our platform.</p>
  <p>StageLoop is not yet ready to host gigs as we're currently working on building our artists. We are launching for venues in Q4 2019. Pre-register now to keep informed and be one of the first people to use our platform.</p>
</div>

<!-- contact -->
<div class="abs contact"></div>
<h2 class="abs contact-title" style="font-family:'Cabin',sans-serif;font-weight:400;line-height:1">Get In touch</h2>
<div class="abs line-field" style="left:187px;top:3372px;width:381px;padding-left:10px">Name</div>
<div class="abs line-field" style="left:187px;top:3415px;width:185px;padding-left:10px">Email</div>
<div class="abs line-field" style="left:383px;top:3415px;width:185px;padding-left:10px">Phone</div>
<div class="abs line-field" style="left:187px;top:3455px;width:381px;height:70px;padding-left:10px">Message</div>
<div class="abs send">SEND MESSAGE</div>

<div class="abs info">
  <svg width="26" height="40" viewBox="0 0 26 40" style="margin-top:94px"><rect x="2" y="2" width="22" height="36" rx="3" fill="none" stroke="#888" stroke-width="3"/><rect x="6" y="7" width="14" height="22" fill="#888"/><circle cx="13" cy="33" r="1.8" fill="#888"/></svg>
  <p class="phone">(555) 014-2270</p>
  <p class="row"><b>Address</b> 48 Harbor Lane, Millbrook, OR, 97000</p>
  <p class="row" style="margin-top:18px"><b>Email</b> hello@stageloop.example</p>
</div>

<footer class="abs footer">© 2019 StageLoop</footer>

</body>
</html>
```